"Sun On Water" Gospel Presentation Booklet

I need a design for a 12 page (including front/back cover) square booklet, with religious images and aesthetically pleasing fonts/designs. I want it to be very simple, and very straightforward. The main focus of the project is it's content. So the design should be very nice, but also should point to the content, not take away from it, or create distraction. People should be more focused on the words than the imagery.

I enjoy modern designs, I need a sharp aesthetic that is clean and neat. Nothing over the top.
I have attached a word document with the content I would like on the pages.

Colors
0592cd
0255a3
33a6d7
85cae6
85acd3
3276b5
9bcb3b
f04a50
f68d4c

Requirements
Should not have
• Super feminine colors/aesthetics

```html
<!DOCTYPE html>
<html lang="en">
<head>
<meta charset="utf-8">
<title>Sun On Water — Man</title>
<link href="https://fonts.googleapis.com/css2?family=Archivo:wdth,wght@75,900&family=Inter:wght@400;700;800&display=swap" rel="stylesheet">
<style>
  :root {
    --backdrop: #e9e9e9;
    --paper: #f4f4f4;
    --ink: #0b0b0b;
    --accent: #ec935f;
    --accent-deep: #e4844d;
    --on-accent: #ffffff;
    --photo-light: #d8d8d8;
    --photo-dark: #2a2a2a;
  }
  * { box-sizing: border-box; margin: 0; padding: 0; }
  html, body {
    width: 1200px;
    height: 768px;
    overflow: hidden;
    background: var(--backdrop);
  }
  .spread {
    position: absolute;
    left: 60px;
    top: 114px;
    width: 1080px;
    height: 540px;
    display: flex;
    box-shadow: 0 10px 30px rgba(0,0,0,0.12);
  }
  .page {
    position: relative;
    width: 540px;
    height: 540px;
    overflow: hidden;
  }
  .page--title {
    background: linear-gradient(90deg, var(--paper) 80%, #e6e6e6 100%);
  }
  .section-word {
    position: absolute;
    left: 20px;
    right: 20px;
    top: 145px;
    text-align: center;
    white-space: nowrap;
    font-family: "Archivo", sans-serif;
    font-stretch: 75%;
    font-weight: 900;
    font-size: 220px;
    line-height: 1;
    letter-spacing: -2px;
    color: var(--ink);
  }
  .page--statement {
    background: linear-gradient(135deg, var(--accent-deep) 0%, var(--accent) 60%);
    color: var(--on-accent);
    font-family: "Inter", sans-serif;
  }
  .statement-heading {
    position: absolute;
    left: 150px;
    top: 120px;
    font-size: 20px;
    font-weight: 800;
    line-height: 1.1;
    text-transform: uppercase;
    letter-spacing: -0.3px;
  }
  .figure-photo {
    position: absolute;
    left: 160px;
    top: 190px;
    width: 110px;
    height: 290px;
    border-radius: 40px 40px 8px 8px;
    background: linear-gradient(180deg, var(--photo-dark) 0%, var(--photo-light) 25%, var(--photo-light) 50%, var(--photo-dark) 60%);
  }
  .statement-body {
    position: absolute;
    left: 285px;
    top: 210px;
    font-size: 17px;
    line-height: 1.2;
    font-weight: 400;
  }
  .statement-body strong {
    font-weight: 800;
    text-transform: uppercase;
  }
</style>
</head>
<body>
  <main class="spread">
    <section class="page page--title">
      <h1 class="section-word">MAN</h1>
    </section>
    <section class="page page--statement">
      <h2 class="statement-heading">On the other hand,<br>mankind is corrupt.</h2>
      <div class="figure-photo" role="img" aria-label="Black and white photo of a young man walking away, seen from above, casting a long shadow"></div>
      <p class="statement-body">
        For example,<br>
        we are <strong>selfish</strong>,<br>
        we are <strong>prideful</strong>,<br>
        and we <strong>lie</strong>.
      </p>
    </section>
  </main>
</body>
</html>
```